Luminously Grounded Vitality

We want to design a business card that is modern and appealing for an innovative psychedelic telemedicine company that provides at-home ketamine-assisted therapy along with wellness, longevity, and anti-aging medicines. We want to use our deep purple and white plus other colors you can find on our website. We don't have any strict brand guidelines yet so feel free to get creative. We want a very professional, but technology first modern design that will instill trust, peace, calm, but also be attractive to investors in the healthcare and SaaS space.

```html
<!DOCTYPE html>
<html lang="en">
<head>
<meta charset="utf-8">
<title>Luminously Grounded Vitality — Business Card</title>
<link href="https://fonts.googleapis.com/css2?family=Marcellus&family=Outfit:wght@600&family=Fira+Sans:wght@400&display=swap" rel="stylesheet">
<style>
  :root {
    --backdrop: #474747;
    --card-base: #12041d;
    --wave-dark: #1e0e31;
    --wave-mid: #4a3866;
    --wave-light: #9083b8;
    --ink-lavender: #9a86c4;
    --shadow: rgba(0, 0, 0, 0.55);
  }
  * { margin: 0; padding: 0; box-sizing: border-box; }
  html, body {
    width: 1200px;
    height: 1000px;
    overflow: hidden;
    background: var(--backdrop);
  }
  .card {
    position: absolute;
    left: 267px;
    width: 666px;
    height: 382px;
    border-radius: 36px;
    background: var(--card-base);
    overflow: hidden;
    box-shadow: 6px 8px 10px var(--shadow);
  }
  .card--front { top: 59px; }
  .card--back { top: 561px; }
  .card__wave {
    position: absolute;
    inset: 0;
    width: 100%;
    height: 100%;
  }
  .card__wave path {
    filter: drop-shadow(10px 12px 14px rgba(0, 0, 0, 0.75));
  }
  .brand {
    position: absolute;
    left: 355px;
    transform: translateX(-50%);
    text-align: center;
    color: var(--ink-lavender);
  }
  .brand__mark {
    position: absolute;
    left: 355px;
    top: 140px;
    width: 84px;
    height: 84px;
    margin-left: -42px;
    border-radius: 50%;
    background: var(--ink-lavender);
  }
  .brand__name {
    top: 268px;
    white-space: nowrap;
    font-family: "Marcellus", serif;
    font-size: 30px;
    line-height: 1;
  }
  .person {
    position: absolute;
    right: 44px;
    top: 124px;
    font-family: "Outfit", sans-serif;
    font-weight: 600;
    font-size: 31px;
    letter-spacing: 1px;
    color: var(--ink-lavender);
  }
  .contact {
    position: absolute;
    right: 40px;
    top: 213px;
    list-style: none;
    font-family: "Fira Sans", sans-serif;
    font-size: 18px;
    letter-spacing: 1.6px;
    color: var(--ink-lavender);
  }
  .contact__item {
    display: flex;
    justify-content: flex-end;
    align-items: center;
    height: 37px;
  }
  .contact__icon {
    width: 22px;
    height: 22px;
    margin-left: 16px;
    fill: var(--ink-lavender);
  }
</style>
</head>
<body>

<svg width="0" height="0" style="position:absolute">
  <defs>
    <linearGradient id="wave-gradient" x1="0" y1="0" x2="1" y2="0">
      <stop offset="0" stop-color="#1e0e31"/>
      <stop offset="0.5" stop-color="#4a3866"/>
      <stop offset="1" stop-color="#9083b8"/>
    </linearGradient>
  </defs>
</svg>

<section class="card card--front">
  <svg class="card__wave" viewBox="0 0 1164 668" preserveAspectRatio="none" aria-hidden="true">
    <path fill="url(#wave-gradient)" d="M0 0 H610 C650 0 668 30 668 65 C668 100 645 131 610 131 C540 133 490 128 440 120 C330 104 220 110 135 180 C100 210 95 270 130 296 C210 352 240 420 234 500 C228 590 180 650 120 668 H0 Z"/>
  </svg>
  <div class="brand__mark"></div>
  <div class="brand brand__name">Luminously Grounded Vitality</div>
</section>

<section class="card card--back">
  <svg class="card__wave" viewBox="0 0 1164 668" preserveAspectRatio="none" aria-hidden="true">
    <path fill="url(#wave-gradient)" d="M0 0 H610 C650 0 668 30 668 65 C668 100 645 131 610 131 C540 133 490 128 440 120 C330 104 220 110 135 180 C100 210 95 270 130 296 C210 352 240 420 234 500 C228 590 180 650 120 668 H0 Z"/>
  </svg>
  <h1 class="person">MARA QUINLEY</h1>
  <ul class="contact">
    <li class="contact__item">
      <span>(555) 014- 2290</span>
      <svg class="contact__icon" viewBox="0 0 24 24" aria-hidden="true"><path d="M6.6 2.2c.6-.3 1.3 0 1.6.6l1.8 3.8c.3.6.1 1.2-.4 1.6L8 9.4c1.1 2.6 3.9 5.4 6.6 6.6l1.2-1.6c.4-.5 1.1-.7 1.6-.4l3.8 1.8c.6.3.9 1 .6 1.6l-.9 2.3c-.4.9-1.3 1.5-2.3 1.4C9.7 20.6 3.4 14.3 2.9 5.4 2.8 4.4 3.4 3.5 4.3 3.1z"/></svg>
    </li>
    <li class="contact__item">
      <span>luminouslygrounded.com</span>
      <svg class="contact__icon" viewBox="0 0 24 24" aria-hidden="true"><path d="M2 6.5C2 5.7 2.7 5 3.5 5h17c.8 0 1.5.7 1.5 1.5v.4l-10 6.3L2 6.9z"/><path d="M2 9.2l10 6.3 10-6.3v8.3c0 .8-.7 1.5-1.5 1.5h-17c-.8 0-1.5-.7-1.5-1.5z"/></svg>
    </li>
    <li class="contact__item">
      <span>mara@luminouslygrounded.com</span>
      <svg class="contact__icon" viewBox="0 0 24 24" aria-hidden="true"><g fill="none" stroke="#9a86c4" stroke-width="1.6"><circle cx="12" cy="12" r="10"/><ellipse cx="12" cy="12" rx="4.5" ry="10"/><path d="M12 2v20M2 12h20M3.5 7h17M3.5 17h17"/></g></svg>
    </li>
  </ul>
</section>

</body>
</html>
```